Logo + Label Design (Men’s Grooming Brand & Product Packaging)

Design a logo and 2 oz pomade label for Brant, a modern men’s grooming brand focused on clean, high-quality, natural ingredients. The design should establish a bold, masculine, minimalist identity that can later extend to products like shaving gel and body wash.

Key Requirements

Create a primary logo for “Brant” and a core label for the 2 oz pomade jar (screw-top).

Use a clean, modern style — masculine, confident, and approachable (think Wendel’s, Valto, Northfield Mill).

Design for 1–2 color screen printing on solid jar colors (white, black, or navy).

Avoid gradients, foil, or embossing. Must work in black & white.

Provide: vector logo, mockup of the 2 oz jar, color palette (CMYK/RGB/HEX), and font specs.

Winning design may lead to future projects (body wash, shave gel, skincare lines).

Font styles to use
Other font styles liked:
• We like the fonts and design concept in the attached mockup.

Requirements
Should not have
• We want to avoid too much writing or busy designs. We want to avoid having graphics/illustrations embedded in the logo if they will cause the brand to look less classy or sophisticated. We also want the design to look simple and all-American (e.g. Pellham and Stroud, Tall Pine, The BRIM, etc). We’d like to give a Kessler & Dunmore vibe that feels classy and high end.

```html
<!DOCTYPE html>
<html lang="en">
<head>
<meta charset="utf-8">
<title>Brant — Logo and Pomade Label</title>
<link rel="stylesheet" href="https://fonts.googleapis.com/css2?family=Archivo+Black&family=Roboto:ital,wght@1,300&family=Roboto+Condensed:wght@400&family=Montserrat:wght@700&display=swap">
<style>
  :root {
    --ink: #231f20;
    --paper: #ffffff;
    --label-top: #fbfbfb;
    --label-bottom: #e4e4e4;
    --gold: #d9b750;
  }
  html, body {
    margin: 0;
    padding: 0;
    width: 1200px;
    height: 1048px;
    overflow: hidden;
    background: var(--paper);
  }
  .artboard {
    display: block;
    width: 1200px;
    height: 1048px;
  }
  .wordmark {
    font-family: "Archivo Black", sans-serif;
    fill: var(--ink);
  }
  .product-name {
    font-family: "Roboto", sans-serif;
    font-style: italic;
    font-weight: 300;
    fill: var(--ink);
  }
  .variant-tag {
    font-family: "Roboto Condensed", sans-serif;
    font-weight: 400;
    fill: var(--paper);
  }
  .net-weight {
    font-family: "Montserrat", sans-serif;
    font-weight: 700;
    fill: var(--ink);
    letter-spacing: 1px;
  }
</style>
</head>
<body>
<svg class="artboard" viewBox="0 0 1200 1048" xmlns="http://www.w3.org/2000/svg">
  <defs>
    <linearGradient id="label-face" x1="0" y1="0" x2="0" y2="1">
      <stop offset="0" stop-color="var(--label-top)"/>
      <stop offset="0.55" stop-color="#f7f7f7"/>
      <stop offset="1" stop-color="var(--label-bottom)"/>
    </linearGradient>
    <clipPath id="half-moon-clip">
      <rect x="426" y="480" width="220" height="460"/>
    </clipPath>
  </defs>

  <!-- Primary logo -->
  <g class="primary-logo">
    <text class="wordmark" x="360" y="312" font-size="150" text-anchor="middle">Brant</text>
  </g>

  <!-- Lid label -->
  <g class="lid-label">
    <circle class="label-disc" cx="360" cy="707" r="221" fill="url(#label-face)"/>
    <circle class="half-moon" cx="360" cy="707" r="197" fill="var(--ink)" clip-path="url(#half-moon-clip)"/>

    <text class="wordmark" x="300" y="698" font-size="68" text-anchor="middle">Brant</text>

    <text class="product-name" x="296" y="756" font-size="18.5" text-anchor="middle">MEN’S HAIR POMADE</text>

    <rect class="variant-bar" x="236" y="762" width="121" height="16" fill="var(--ink)"/>
    <text class="variant-tag" x="296.5" y="775" font-size="12.5" text-anchor="middle">FRESH &amp; CLEAN</text>

    <text class="net-weight" x="307" y="838" font-size="10" text-anchor="middle">2 oz / 57 g</text>
  </g>
</svg>
</body>
</html>
```